Etiketten für verschiedene Lebensmittel
Zielgruppe
Verkauf von Lebensmitteln über das Internet, direkt und über Lebensmittelautomaten
Aufgabenstellung
Es soll die Verbindung zur Landwirtschaft behalten werden, das Etikett soll eine Fusion von Tradition und Professionalität darstellen.
Das Logo ist vorhanden, wird angehängt. (Logo.png)
Das Logo für die Automaten ist nur sekundär, habe es aber auch angehängt (frischkastenlogo.jpg)
Die (noch nicht fertige) Homepage ist hier:
http://landwirtschaft.brennhofer.at/
Der Umfang wird erweitert, brauchen mehrere Etiketten mit der selben Richtung.
Wir starten mit Fleisch, dann wird bei erfolgreicher Zusammenarbeit auf mehrere andere erweitert, unter anderem andere Fleischsorten, Öl und Hanfmehlprodukte.
Das Preisgeld wird mit diesen weiteren Projekten natürlich auch erweitert.
Mehr Informationen für das Fleischetikett:
Das Etikett wird auf vakuumverpacktes Fleisch geklebt.
Vom Format sind wir flexibel, beim Fleisch soll es aber eher in Richtung Quadratisch gehen (ist aber nicht zwingend).
Informationen auf dem Etikett sind:
- Fleischsorte: (Schnitzel, Kotlett, Speck, Braten usw.) --> sollte leicht austauschbar sein, da wir das Etikett für alle Fleischsorten nutzen wollen.
- Inhaltsstoffe: Die Inhaltsstoffe sind sehr wenige, da es sich um rohes Fleisch handelt, bei marinierten Produkten und dem Speck brauchen wir diese jedoch.
- Ablaufdatum und Füllmenge: Diese zwei informationen werden dann beim Druck erst geliefert, geplant ist ein Programm das die Informationen direkt vor dem Druck aktualisiert
- Größe des Etikettes: 8-12cm Durchmesser, grob geschätzt, wir sind da auch flexibel da wir die Etiketten selbst drucken
- Das frischkasten Logo soll nicht eingebaut werden in diesem Etikett, werde das entfernen vom Anhang um Missverständnisse zu vermeiden
- Es handelt sich um Bio Schweinefleisch (hatte vergessen das anzumerken)
Habe das Brennhofer Logo auf eine bessere Auflösung geupdated
Auch andere kleinere Designs werden benötigt, wir freuen uns auf eine ..

```html
<!DOCTYPE html>
<html lang="de">
<head>
<meta charset="utf-8">
<title>Biohof Brennhofer – Fleischetiketten</title>
<link rel="stylesheet" href="https://fonts.googleapis.com/css2?family=Mulish:ital,wght@0,600;0,700;0,800;1,400&family=PT+Sans:ital,wght@0,700;1,700&family=Arimo:wght@700&display=swap">
<style>
  :root {
    --backdrop: #d6d6d6;
    --label-bg: #1d1d1d;
    --glow: #3a3a3a;
    --brand-green: #8a9a4c;
    --accent-red: #e3001b;
    --text-light: #f2f2f2;
    --sketch-tone: #8c8c8c;
  }
  * { box-sizing: border-box; margin: 0; padding: 0; }
  html, body {
    width: 1200px; height: 720px; overflow: hidden;
    background: var(--backdrop);
  }
  .sheet { position: relative; width: 1200px; height: 720px; }
  .label {
    position: absolute; top: 47px;
    width: 481px; height: 623px;
    background: var(--label-bg);
    box-shadow: 3px 4px 6px rgba(0,0,0,.35);
    overflow: hidden;
  }
  .label--marinated { left: 91px; }
  .label--plain { left: 613px; }

  .brand {
    position: absolute; top: 62px; left: 0; width: 100%;
    display: flex; justify-content: center; align-items: center; gap: 10px;
    font-family: "Mulish", sans-serif; font-weight: 600;
    font-size: 34px; color: var(--brand-green);
  }
  .brand__dot {
    width: 14px; height: 14px; border-radius: 50%;
    background: var(--brand-green);
  }

  .artwork {
    position: absolute; left: 70px; top: 176px;
    width: 370px; height: 380px;
    border-radius: 50%;
    background: radial-gradient(circle at 50% 50%, var(--sketch-tone) 0%, #5a5a5a 40%, var(--glow) 62%, rgba(29,29,29,0) 75%);
  }

  .product-seal {
    position: absolute; left: 122px; top: 240px;
    width: 232px; height: 232px;
  }
  .product-seal svg { position: absolute; inset: 0; }
  .product-seal__text {
    position: absolute; inset: 0;
    text-align: center; color: var(--accent-red);
  }
  .product-name {
    font-family: "PT Sans", sans-serif; font-weight: 700; font-style: italic;
    font-size: 31px; line-height: 32px;
    position: absolute; left: 0; width: 100%;
  }
  .product-variant {
    font-family: "Mulish", sans-serif; font-style: italic; font-weight: 400;
    font-size: 20px; position: absolute; left: 0; width: 100%; top: 118px;
  }
  .fill-label {
    position: absolute; left: 0; width: 100%; top: 170px;
    font-family: "Mulish", sans-serif; font-style: italic; font-weight: 400;
    font-size: 13px; color: var(--text-light);
  }
  .fill-amount {
    position: absolute; left: 0; width: 100%; top: 188px;
    font-family: "Arimo", sans-serif; font-weight: 700;
    font-size: 21px; color: #fff;
  }

  .ingredients {
    position: absolute; left: 23px; top: 561px;
    font-family: "Mulish", sans-serif; font-style: italic; font-weight: 400;
    font-size: 13px; line-height: 17px; color: var(--text-light);
  }
  .expiry {
    position: absolute; right: 26px; top: 592px;
    font-family: "Mulish", sans-serif; color: var(--text-light);
    font-size: 13px; white-space: nowrap;
  }
  .expiry__label { font-style: italic; font-weight: 400; }
  .expiry__date { font-weight: 800; font-size: 16px; margin-left: 4px; }
</style>
</head>
<body>
<main class="sheet">

  <article class="label label--marinated">
    <div class="brand"><span class="brand__dot"></span>Biohof Brennhofer</div>
    <div class="artwork" role="img" aria-label="Kreidezeichnung von Fleischstücken, Würsten und Kräutern rund um das Produktsiegel"></div>
    <div class="product-seal">
      <svg viewBox="0 0 232 232" aria-hidden="true">
        <circle cx="116" cy="116" r="112" fill="var(--label-bg)" stroke="var(--accent-red)" stroke-width="5"/>
      </svg>
      <div class="product-seal__text">
        <div class="product-name" style="top:54px">Bio<br>Kotelett</div>
        <div class="product-variant">mariniert</div>
        <div class="fill-label">Füllmenge</div>
        <div class="fill-amount">300 g</div>
      </div>
    </div>
    <p class="ingredients">Zutaten: Meersalz,<br>Knoblauch, Paprika,<br>Rosmarin, grüner Pfeffer</p>
    <p class="expiry"><span class="expiry__label">Ablaufdatum</span><span class="expiry__date">06.05.2017</span></p>
  </article>

  <article class="label label--plain">
    <div class="brand"><span class="brand__dot"></span>Biohof Brennhofer</div>
    <div class="artwork" role="img" aria-label="Kreidezeichnung von Fleischstücken, Würsten und Kräutern rund um das Produktsiegel"></div>
    <div class="product-seal">
      <svg viewBox="0 0 232 232" aria-hidden="true">
        <circle cx="116" cy="116" r="112" fill="var(--label-bg)" stroke="var(--accent-red)" stroke-width="5"/>
      </svg>
      <div class="product-seal__text">
        <div class="product-name" style="top:58px">Bio<br>Kotelett</div>
        <div class="fill-label">Füllmenge</div>
        <div class="fill-amount">300 g</div>
      </div>
    </div>
    <p class="expiry"><span class="expiry__label">Ablaufdatum</span><span class="expiry__date">06.05.2017</span></p>
  </article>

</main>
</body>
</html>
```